Flyer-Design für Weihnachtsbäume als Dekoration
Zielgruppe
Wir bearbeiten Bleche nach Kundenvorgaben. Nebenbei stellen wir immer mal ein paar Dekoartikel
bzw. Sonderanfertigen her.
https://feinblechwerk-muster.de/
http://www.talbergwerk.de/
https://feinblechwerk-muster.de/aktuelles/image-broschuere/
Mit diesem Flyer wollen wir für unsere Weihnachtsbäume werben. Die Preise sind Endpreis inkl. Mehrwertsteuer.
Aufgabenstellung
Ich hab noch mehr Bildmaterial zur Verfügung.

```html
<!DOCTYPE html>
<html lang="de">
<head>
<meta charset="utf-8">
<title>Xmas Tree – Weihnachtsbäume Flyer</title>
<link rel="stylesheet" href="https://fonts.googleapis.com/css2?family=Abel&family=Kaushan+Script&display=swap">
<style>
  :root {
    --stage: #ececec;
    --stage-light: #f7f7f7;
    --paper: #ffffff;
    --gold: #d4b96b;
    --gold-deep: #b99a5b;
    --gold-dark: #5a4a2c;
    --text-light: #fffaf0;
    --photo-light: #e9e8e6;
    --photo-mid: #c9c6c1;
    --photo-warm: #a88a6c;
  }
  * { box-sizing: border-box; margin: 0; padding: 0; }
  html, body { width: 1200px; height: 800px; overflow: hidden; }
  body {
    background: radial-gradient(ellipse at 70% 80%, var(--stage-light), var(--stage) 75%);
    font-family: "Abel", sans-serif;
  }
  .flyer-spread {
    position: absolute;
    left: 250px; top: 82px;
    width: 700px; height: 636px;
    display: flex;
    box-shadow: 0 14px 30px rgba(0,0,0,.12);
  }
  .cover-page {
    width: 408px; height: 100%;
    background: var(--paper);
    padding: 12px;
    position: relative;
  }
  .cover-photo {
    width: 100%; height: 100%;
    background:
      radial-gradient(circle at 30% 45%, #f5f4f2 0 22%, transparent 45%),
      radial-gradient(circle at 78% 30%, #fbfbfa 0 18%, transparent 35%),
      linear-gradient(160deg, var(--photo-light) 0%, var(--photo-mid) 55%, var(--photo-warm) 78%, #6d6157 100%);
  }
  .title-badge {
    position: absolute;
    left: 140px; top: 290px;
    width: 170px; height: 170px;
    border-radius: 50%;
    background: rgba(212,185,107,.9);
    display: flex; flex-direction: column;
    align-items: center; justify-content: center;
    color: var(--paper);
    font-family: "Kaushan Script", cursive;
    line-height: .95;
  }
  .title-badge .title-line-1 { font-size: 44px; transform: translateX(-10px); }
  .title-badge .title-line-2 { font-size: 40px; transform: translateX(14px); }
  .info-page {
    width: 292px; height: 100%;
    background: var(--gold);
    position: relative;
    padding: 36px 28px 0 30px;
    color: var(--text-light);
  }
  .info-heading {
    font-size: 22px;
    letter-spacing: .5px;
    font-weight: 400;
    margin-bottom: 18px;
  }
  .info-text {
    font-size: 12.5px;
    line-height: 1.45;
    margin-bottom: 14px;
  }
  .product-photo-frame {
    position: absolute;
    left: 24px; top: 218px;
    width: 268px; height: 250px;
    background: var(--gold-deep);
    padding: 8px 0 8px 8px;
  }
  .product-photo {
    width: 100%; height: 100%;
    background:
      radial-gradient(circle at 40% 55%, #ffffff 0 25%, transparent 50%),
      linear-gradient(170deg, #f3f2f0 0%, #dcdad6 60%, #b49a7c 100%);
  }
  .brand-row {
    position: absolute;
    left: 30px; right: 20px; bottom: 40px;
    display: flex; align-items: flex-end; justify-content: space-between;
    color: var(--gold-dark);
  }
  .brand-name { font-size: 17px; }
  .brand-block { text-align: right; }
  .brand-tagline { font-size: 7px; letter-spacing: 1.5px; text-transform: uppercase; margin-top: 3px; }
  .bottom-rule {
    position: absolute;
    left: 0; right: 0; bottom: 20px;
    height: 2px; background: var(--paper);
  }
</style>
</head>
<body>
  <main class="flyer-spread">
    <section class="cover-page">
      <div class="cover-photo" role="img" aria-label="Foto: weiße Metall-Weihnachtsbäume mit Kugeln, Sternen-Windlicht, Schneemann und Rentier-Deko"></div>
      <div class="title-badge">
        <span class="title-line-1">Xmas</span>
        <span class="title-line-2">Tree</span>
      </div>
    </section>
    <section class="info-page">
      <h1 class="info-heading">WEIHNACHTSBÄUME</h1>
      <p class="info-text">In Vorbereitung auf bestimmte Festlichkeiten wird unser Service gern genutzt. Ein schöner Blickfang als Dekoration für Innen und Außen.</p>
      <p class="info-text">Kontaktieren Sie uns zur Erfüllung Ihrer maßgeschneiderten Wünsche!</p>
      <div class="product-photo-frame">
        <div class="product-photo" role="img" aria-label="Foto: weiße Metall-Weihnachtsbäume mit silbernen Kugeln"></div>
      </div>
      <div class="brand-row">
        <span class="brand-name">Feinblechwerk</span>
        <div class="brand-block">
          <div class="brand-name">Talbergwerk</div>
          <div class="brand-tagline">Laserschnitt &amp; Kantentechnik</div>
        </div>
      </div>
      <div class="bottom-rule"></div>
    </section>
  </main>
</body>
</html>
```